Open Horizon; Teaching Series Art.

Our church is going to be teaching a series of messages under the topic/title: Open Horizon. Just looking for a simple design to help with this. I have uploaded a design that is an example of what we were thinking.

The point of the design is to communicate a new way of doing things (given some of the impact of the coronavirus) - although the background doesn't need to be too busy - just something simple, clean and modern.

Even though it's for a church, we don't need any religious art in the background (crosses, people praying, etc.) Looking for a similar feel background to the one we uploaded.

The only text should be Open Horizon and maybe highlighting the word Open somehow.

Font styles to use
Sans Serif

Requirements
Must have
• Title of "Open Horizon" - no other text.

```html
<!DOCTYPE html>
<html lang="en">
<head>
<meta charset="utf-8">
<title>Open Horizon</title>
<link rel="stylesheet" href="https://fonts.googleapis.com/css2?family=Dosis:wght@700;800&display=swap">
<style>
  :root {
    --red-deep: #7e0a0d;
    --red-mid: #b3141a;
    --red-bright: #e4202a;
    --yellow: #fde93a;
    --white: #ffffff;
    --title-red: #d8141c;
  }
  html, body {
    margin: 0;
    padding: 0;
    overflow: hidden;
    background: var(--red-deep);
  }
  .poster {
    position: relative;
    width: 851px;
    height: 1200px;
    overflow: hidden;
    font-family: "Dosis", "Arial Rounded MT Bold", sans-serif;
  }
  .backdrop {
    position: absolute;
    inset: 0;
    width: 851px;
    height: 1200px;
  }
  .title {
    position: absolute;
    left: 0;
    top: 0;
    width: 851px;
    height: 1200px;
  }
  .title__tag {
    position: absolute;
    left: 282px;
    top: 468px;
    padding: 0 18px;
    height: 84px;
    background: var(--yellow);
    color: var(--title-red);
    font-weight: 700;
    font-size: 86px;
    line-height: 88px;
    letter-spacing: 1px;
    transform: rotate(-4deg);
    transform-origin: left bottom;
  }
  .title__main {
    position: absolute;
    left: 0;
    width: 851px;
    top: 540px;
    text-align: center;
    color: var(--white);
    font-weight: 800;
    font-size: 148px;
    line-height: 160px;
    letter-spacing: 2px;
    margin: 0;
  }
</style>
</head>
<body>
  <main class="poster">
    <svg class="backdrop" viewBox="0 0 851 1200" xmlns="http://www.w3.org/2000/svg">
      <defs>
        <linearGradient id="base-red" x1="0" y1="0" x2="1" y2="0.35">
          <stop offset="0" stop-color="var(--red-deep)"/>
          <stop offset="0.55" stop-color="var(--red-mid)"/>
          <stop offset="1" stop-color="var(--red-bright)"/>
        </linearGradient>
        <radialGradient id="center-glow" cx="0.5" cy="0.5" r="0.5">
          <stop offset="0" stop-color="#f03038" stop-opacity="0.45"/>
          <stop offset="1" stop-color="#f03038" stop-opacity="0"/>
        </radialGradient>
        <linearGradient id="streak" x1="0" y1="0" x2="1" y2="0">
          <stop offset="0" stop-color="#ffffff" stop-opacity="0"/>
          <stop offset="0.5" stop-color="#ffffff" stop-opacity="0.07"/>
          <stop offset="1" stop-color="#ffffff" stop-opacity="0"/>
        </linearGradient>
      </defs>
      <rect width="851" height="1200" fill="url(#base-red)"/>
      <g class="light-streaks">
        <polygon points="380,0 520,0 851,260 851,380" fill="url(#streak)"/>
        <polygon points="560,0 640,0 851,150 851,210" fill="url(#streak)"/>
        <polygon points="0,940 0,1010 420,1200 300,1200" fill="url(#streak)"/>
        <polygon points="0,1050 0,1090 220,1200 150,1200" fill="url(#streak)"/>
      </g>
      <ellipse role="img" aria-label="Soft halftone dot texture behind the title" cx="430" cy="560" rx="400" ry="440" fill="url(#center-glow)"/>
    </svg>

    <h1 class="title" aria-label="Open Horizon">
      <span class="title__tag">OPEN</span>
      <span class="title__main">HORIZON</span>
    </h1>
  </main>
</body>
</html>
```